Professional window cleaning services business needs a flyer design

We are looking to attract large businesses such as gyms, car dealerships and fast food restaurants.
-Have over 15 years of experience in this business
-We serve customers in Melbourne and all surrounding suburbs
-Specialising in automated periodical services(daily,weekly,monthly, yearly)
-Our current client base consists of major fast food restaurants, car dealerships and residential properties.

Industry/Entity Type

Window Cleaning

Colors
3176b5
fbed22

Requirements
Must have
• Business Details:
• Name: Brisk Window Cleaning
• Phone no:94530617
• website:www.briskservices.com.au
• email: admin@briskservices.com.au
• mail: PO BOX 2748, Wattlebrook North, 3187

```html
<!DOCTYPE html>
<html lang="en">
<head>
<meta charset="utf-8">
<title>Brisk Window Cleaning Flyer</title>
<link rel="stylesheet" href="https://fonts.googleapis.com/css2?family=Archivo+Black&family=Open+Sans:wdth,wght@75..100,400..600&family=Roboto+Condensed:wght@700&display=swap">
<style>
  :root {
    --brand-blue: #0f4a8c;
    --title-blue: #0d4689;
    --brand-yellow: #fbd21c;
    --accent-orange: #e8872a;
    --ink: #1c1c1c;
    --white: #ffffff;
    --stage: #e9e9e9;
  }
  html, body {
    margin: 0;
    padding: 0;
    width: 941px;
    height: 1200px;
    overflow: hidden;
    background: var(--stage);
  }
  .flyer {
    position: absolute;
    left: 50px;
    top: 0;
    width: 841px;
    height: 1200px;
    background: var(--white);
    overflow: hidden;
    font-family: "Open Sans", sans-serif;
  }
  .title {
    position: absolute;
    left: 40px;
    top: 24px;
    margin: 0;
    font-family: "Archivo Black", sans-serif;
    font-weight: 400;
    font-size: 55px;
    line-height: 76px;
    color: var(--title-blue);
    letter-spacing: 0.5px;
    white-space: nowrap;
  }
  .tagline {
    position: absolute;
    left: 40px;
    top: 106px;
    margin: 0;
    font-size: 22px;
    line-height: 29px;
    color: var(--ink);
    text-transform: uppercase;
    white-space: nowrap;
  }
  .rule {
    position: absolute;
    left: 0;
    top: 182px;
    width: 841px;
    height: 5px;
    background: linear-gradient(90deg, #f7e31c, var(--brand-yellow) 60%, var(--accent-orange));
  }
  .hero {
    position: absolute;
    left: 0;
    top: 187px;
    width: 841px;
    height: 421px;
    background: linear-gradient(180deg, #c9d3d8 0%, #9fb08a 35%, #d9c63a 55%, #e2cf33 70%, #6f6f68 100%);
  }
  .call {
    position: absolute;
    left: 92px;
    top: 512px;
    margin: 0;
    font-family: "Roboto Condensed", sans-serif;
    font-weight: 700;
    font-size: 45px;
    line-height: 56px;
    color: var(--white);
    text-shadow: 0 2px 4px rgba(0,0,0,0.55);
    white-space: nowrap;
  }
  .experience {
    position: absolute;
    right: 22px;
    top: 549px;
    margin: 0;
    text-align: right;
    font-family: "Roboto Condensed", sans-serif;
    font-weight: 700;
    font-size: 19px;
    line-height: 25px;
    color: var(--white);
    text-shadow: 0 1px 3px rgba(0,0,0,0.6);
    white-space: nowrap;
  }
  .web-tab {
    position: absolute;
    left: 49px;
    top: 574px;
    width: 418px;
    height: 46px;
  }
  .web-tab svg { position: absolute; inset: 0; }
  .web-tab span {
    position: relative;
    display: block;
    text-align: center;
    font-family: "Roboto Condensed", sans-serif;
    font-weight: 700;
    font-size: 25px;
    line-height: 46px;
    letter-spacing: 1px;
    color: var(--ink);
    white-space: nowrap;
  }
  .panel {
    position: absolute;
    left: 0;
    top: 608px;
    width: 841px;
    height: 592px;
    background: var(--brand-blue);
    color: var(--white);
  }
  .services-heading {
    position: absolute;
    left: 40px;
    top: 37px;
    margin: 0;
    font-weight: 400;
    font-size: 29px;
    line-height: 40px;
  }
  .services {
    position: absolute;
    top: 94px;
    margin: 0;
    padding: 0;
    list-style: none;
    font-size: 21px;
  }
  .services.col-a { left: 40px; }
  .services.col-b { left: 308px; }
  .services li {
    display: flex;
    align-items: center;
    height: 32px;
    white-space: nowrap;
  }
  .services svg { width: 22px; height: 22px; margin-right: 15px; flex: none; }
  .seal {
    position: absolute;
    left: 645px;
    top: 10px;
    width: 170px;
    height: 120px;
  }
  .seal-name {
    position: absolute;
    left: 645px;
    top: 130px;
    width: 170px;
    margin: 0;
    text-align: center;
    font-weight: 600;
    font-size: 30px;
    line-height: 40px;
    color: var(--brand-yellow);
  }
  .reach {
    position: absolute;
    left: 43px;
    top: 237px;
    margin: 0;
    font-size: 23px;
    line-height: 32px;
    white-space: nowrap;
  }
  .target-strip {
    position: absolute;
    left: 40px;
    top: 282px;
    width: 749px;
    height: 29px;
    margin: 0;
    background: var(--brand-yellow);
    color: var(--ink);
    font-size: 16.5px;
    font-stretch: 85%;
    line-height: 29px;
    text-align: center;
    white-space: nowrap;
    overflow: hidden;
  }
  .gallery-photo {
    position: absolute;
    top: 328px;
    height: 207px;
    box-shadow: 0 2px 5px rgba(0,0,0,0.4);
  }
  .gallery-photo.building {
    left: 40px;
    width: 422px;
    background: linear-gradient(180deg, #e6eaee 0%, #8aa0b8 40%, #5d7186 70%, #7a8068 100%);
  }
  .gallery-photo.squeegee {
    left: 472px;
    width: 317px;
    background: linear-gradient(135deg, #c5d67a 0%, #9fbb3c 50%, #7f9a2b 100%);
  }
  .contact {
    position: absolute;
    top: 546px;
    margin: 0;
    line-height: 32px;
    white-space: nowrap;
  }
  .contact.email { left: 40px; font-size: 22px; }
  .contact.post { right: 50px; font-size: 18px; }
</style>
</head>
<body>
<main class="flyer">
  <h1 class="title">Brisk Window Cleaning</h1>
  <p class="tagline">Specialising in automated periodical services<br>(Daily-Weekly-Monthly-Yearly)</p>
  <div class="rule"></div>

  <div class="hero" role="img" aria-label="Photo of a technician standing beside the yellow company van with ladders on its roof rack"></div>
  <p class="call">Call Us: 94530617</p>
  <p class="experience">Have over 15 years of<br>experience in this business</p>
  <div class="web-tab">
    <svg viewBox="0 0 418 46" preserveAspectRatio="none" aria-hidden="true">
      <path d="M0 46 L18 8 Q22 0 32 0 L386 0 Q396 0 400 8 L418 46 Z" fill="#fbd21c"/>
    </svg>
    <span>www.briskservices.com.au</span>
  </div>

  <section class="panel">
    <h2 class="services-heading">Services:</h2>
    <ul class="services col-a">
      <li><svg viewBox="0 0 22 22" aria-hidden="true"><rect x="1" y="4" width="17" height="17" fill="none" stroke="#fbd21c" stroke-width="2.5"/><path d="M5 12 L9 17 L20 2" fill="none" stroke="#fbd21c" stroke-width="3"/></svg>High Rise Services</li>
      <li><svg viewBox="0 0 22 22" aria-hidden="true"><rect x="1" y="4" width="17" height="17" fill="none" stroke="#fbd21c" stroke-width="2.5"/><path d="M5 12 L9 17 L20 2" fill="none" stroke="#fbd21c" stroke-width="3"/></svg>Residential Services</li>
      <li><svg viewBox="0 0 22 22" aria-hidden="true"><rect x="1" y="4" width="17" height="17" fill="none" stroke="#fbd21c" stroke-width="2.5"/><path d="M5 12 L9 17 L20 2" fill="none" stroke="#fbd21c" stroke-width="3"/></svg>Corporate Services</li>
      <li><svg viewBox="0 0 22 22" aria-hidden="true"><rect x="1" y="4" width="17" height="17" fill="none" stroke="#fbd21c" stroke-width="2.5"/><path d="M5 12 L9 17 L20 2" fill="none" stroke="#fbd21c" stroke-width="3"/></svg>Pressure Services</li>
    </ul>
    <ul class="services col-b">
      <li><svg viewBox="0 0 22 22" aria-hidden="true"><rect x="1" y="4" width="17" height="17" fill="none" stroke="#fbd21c" stroke-width="2.5"/><path d="M5 12 L9 17 L20 2" fill="none" stroke="#fbd21c" stroke-width="3"/></svg>Commercial Services</li>
      <li><svg viewBox="0 0 22 22" aria-hidden="true"><rect x="1" y="4" width="17" height="17" fill="none" stroke="#fbd21c" stroke-width="2.5"/><path d="M5 12 L9 17 L20 2" fill="none" stroke="#fbd21c" stroke-width="3"/></svg>Gutter Services</li>
      <li><svg viewBox="0 0 22 22" aria-hidden="true"><rect x="1" y="4" width="17" height="17" fill="none" stroke="#fbd21c" stroke-width="2.5"/><path d="M5 12 L9 17 L20 2" fill="none" stroke="#fbd21c" stroke-width="3"/></svg>Roof Services</li>
      <li><svg viewBox="0 0 22 22" aria-hidden="true"><rect x="1" y="4" width="17" height="17" fill="none" stroke="#fbd21c" stroke-width="2.5"/><path d="M5 12 L9 17 L20 2" fill="none" stroke="#fbd21c" stroke-width="3"/></svg>Blind Services / Consulting Services</li>
    </ul>

    <svg class="seal" viewBox="0 0 170 120" aria-hidden="true">
      <circle cx="85" cy="58" r="55" fill="#c9a43a"/>
    </svg>
    <p class="seal-name">BRISK</p>

    <p class="reach">We serve customers in Melbourne and all surrounding suburbs</p>
    <p class="target-strip">We are looking to attract large businesses such as gyms, car dealerships and fast food restaurants</p>

    <div class="gallery-photo building" role="img" aria-label="Photo of a technician cleaning the glass facade of a large commercial building with the company van parked in front"></div>
    <div class="gallery-photo squeegee" role="img" aria-label="Close-up photo of a gloved hand drawing a squeegee across a soapy window"></div>

    <p class="contact email">Email: admin@briskservices.com.au</p>
    <p class="contact post">PO BOX 2748, Wattlebrook North, 3187</p>
  </section>
</main>
</body>
</html>
```